Qorvilo IT Website

We need a logo design for a new company in Jeffersonville, IN (serving predminately the Louisville, KY area). We merged Tarnwell Information Systems (an IT staffing company) and Cobalt Wayfarers (a business intelligence consulting group). Our logo was completed through Brush Market. We are doing a soft launch as we want one web page with just basic information and link that to the existing web pages we have: 1) www.tarnwellinfo.com and 2) www.cobaltwayfarers.com.
The 3 tabs we have in mind are:
Services/News/About Us. Under Services are: IT Staffing, Analytics/BI, Strategic Outsourcing, and CIO Services. Under About Us, we have History, Leadership and Contact Us. No submenu for News.
We also want to have the current companies' sites as clickable links. One should be IT Staffing (directed to www.tarnwellinfo.com) and the other should be Business Intelligence/Data Analytics (directed to www.cobaltwayfarers.com).
Target Market(s)
IT professionals and clients needing IT services
Industry/Entity Type
It Company
Coding
Coded - Design and coding required
Number of Pages Required
4 page
Look and feel

```html
<!DOCTYPE html>
<html lang="en">
<head>
<meta charset="utf-8">
<title>Qorvilo IT</title>
<link rel="stylesheet" href="https://fonts.googleapis.com/css2?family=Montserrat:wght@400;500;600&family=Open+Sans:wght@300;400&display=swap">
<style>
  :root {
    --brand: #1f8fd6;
    --brand-deep: #155f99;
    --accent: #2aa3dc;
    --hero-a: #1a6fae;
    --hero-b: #2489c9;
    --text: #4a4a4a;
    --muted: #8a8a8a;
    --footer: #ececec;
    --white: #ffffff;
  }
  * { margin: 0; padding: 0; box-sizing: border-box; }
  html, body { width: 1006px; height: 1200px; overflow: hidden; background: var(--white); }
  .page { position: relative; width: 1006px; height: 1200px; font-family: "Open Sans", sans-serif; color: var(--text); }

  .site-header { position: absolute; left: 0; top: 0; width: 100%; height: 94px; }
  .brand { position: absolute; left: 94px; top: 24px; }
  .brand-name { font-family: "Montserrat", sans-serif; font-weight: 600; font-size: 32px; color: var(--brand); line-height: 1; }
  .brand-tagline { font-family: "Montserrat", sans-serif; font-weight: 500; font-size: 9px; color: var(--brand); letter-spacing: .5px; margin-top: 5px; }

  .hero { position: absolute; left: 0; top: 94px; width: 100%; height: 485px; }
  .hero-photo { position: absolute; inset: 0; background: linear-gradient(135deg, var(--hero-a), var(--hero-b) 55%, var(--hero-a)); }
  .hero-title { position: absolute; top: 150px; width: 100%; text-align: center; font-family: "Montserrat", sans-serif; font-weight: 600; font-size: 40px; color: var(--white); letter-spacing: .5px; }
  .hero-lead { position: absolute; top: 203px; left: 173px; width: 660px; text-align: center; font-size: 17.5px; line-height: 26px; color: var(--white); }
  .partners { position: absolute; top: 271px; left: 268px; }
  .partner-name { font-family: "Open Sans", sans-serif; font-weight: 400; font-size: 13px; fill: var(--brand-deep); }
  .slider-dots { position: absolute; top: 451px; left: 470px; display: flex; gap: 3px; }
  .slider-dots span { width: 16px; height: 16px; border-radius: 50%; background: var(--white); }
  .slider-dots .active { background: transparent; border: 2px solid var(--white); }

  .team-title { position: absolute; top: 615px; width: 100%; text-align: center; font-family: "Montserrat", sans-serif; font-weight: 400; font-size: 27px; color: var(--brand-deep); letter-spacing: .5px; }
  .member { position: absolute; }
  .portrait { position: absolute; width: 143px; height: 143px; border: 1px solid var(--accent); border-radius: 50%; padding: 6px; }
  .portrait-fill { width: 100%; height: 100%; border-radius: 50%; background: linear-gradient(160deg, #8a8f86, #4d5a5e); }
  .member-info { position: absolute; width: 248px; }
  .member-name { font-family: "Montserrat", sans-serif; font-size: 20px; font-weight: 400; color: var(--brand-deep); line-height: 24px; }
  .member-role { font-size: 15px; color: var(--accent); margin-top: 8px; line-height: 20px; }
  .member-bio { font-size: 10.4px; line-height: 19.2px; color: var(--muted); margin-top: 6px; }
  .learn-more { display: inline-flex; align-items: center; gap: 6px; margin-top: 12px; font-family: "Montserrat", sans-serif; font-size: 12px; color: var(--text); text-decoration: none; }

  .site-footer { position: absolute; left: 0; top: 1121px; width: 100%; height: 79px; background: var(--footer); }
  .copyright { position: absolute; left: 98px; top: 22px; font-size: 11.5px; color: var(--muted); }
  .social { position: absolute; left: 793px; top: 17px; display: flex; gap: 3px; }
  .social span { width: 27px; height: 27px; border: 1.5px solid #777; border-radius: 50%; }
</style>
</head>
<body>
<div class="page">
  <header class="site-header">
    <div class="brand">
      <div class="brand-name">Qorvilo IT</div>
      <div class="brand-tagline">IT STAFFING &amp; ANALYTICS</div>
    </div>
  </header>

  <section class="hero">
    <div class="hero-photo" role="img" aria-label="Team meeting around a table in a bright office, tinted blue"></div>
    <h1 class="hero-title">WELCOME TO QORVILO</h1>
    <p class="hero-lead">Fusce ultricies orci ac feugiat suscipit leo massa sodales velit et scelerisque mi tortor at ipsum cligula augue bibendum accumsan</p>
    <svg class="partners" width="442" height="66" viewBox="0 0 442 66">
      <polygon points="20,0 228,0 208,64 0,64" fill="#fff"/>
      <polygon points="232,0 440,0 420,64 212,64" fill="#fff"/>
      <text class="partner-name" x="112" y="37" text-anchor="middle">Tarnwell Information Systems</text>
      <text class="partner-name" x="326" y="37" text-anchor="middle">Cobalt Wayfarers</text>
    </svg>
    <div class="slider-dots"><span class="active"></span><span></span><span></span><span></span></div>
  </section>

  <h2 class="team-title">OUR TEAM</h2>

  <article class="member" style="left:95px;top:679px">
    <div class="portrait"><div class="portrait-fill" role="img" aria-label="Portrait of the CEO"></div></div>
    <div class="member-info" style="left:155px;top:6px">
      <h3 class="member-name">Derek Holloway</h3>
      <div class="member-role">CEO</div>
      <p class="member-bio">Highly energetic leader with a proven track record in achieving exceptional results through executive level relationship management, consultative selling and creative solutions to complex</p>
      <a class="learn-more" href="#">LEARN MORE <svg width="14" height="10" viewBox="0 0 14 10"><path d="M0 5h12M8 1l4 4-4 4" fill="none" stroke="#2aa3dc" stroke-width="1.4"/></svg></a>
    </div>
  </article>

  <article class="member" style="left:515px;top:686px">
    <div class="portrait"><div class="portrait-fill" role="img" aria-label="Portrait of the COO and CPO" style="background:linear-gradient(160deg,#9a6a4e,#5a4036)"></div></div>
    <div class="member-info" style="left:154px;top:-8px">
      <h3 class="member-name">Maren Ellis</h3>
      <div class="member-role">COO &amp; CPO</div>
      <p class="member-bio">Maren has been in HR and recruiting since 1996 in the IT, engineering and healthcare industries. Prior to coming to Tarnwell, Maren was the Program Director of the BS/MS in HR degree</p>
      <a class="learn-more" href="#">LEARN MORE <svg width="14" height="10" viewBox="0 0 14 10"><path d="M0 5h12M8 1l4 4-4 4" fill="none" stroke="#2aa3dc" stroke-width="1.4"/></svg></a>
    </div>
  </article>

  <article class="member" style="left:95px;top:896px">
    <div class="portrait"><div class="portrait-fill" role="img" aria-label="Portrait of the business development manager" style="background:linear-gradient(160deg,#7f9a7a,#3b4046)"></div></div>
    <div class="member-info" style="left:155px;top:8px">
      <h3 class="member-name">Owen Partridge</h3>
      <div class="member-role">Business Development Manager</div>
      <p class="member-bio">Driven, passionate and empathetic to your business needs, Owen utilizes his 9 years of experience in sales, account management and marketing to achieve results.</p>
      <a class="learn-more" href="#">LEARN MORE <svg width="14" height="10" viewBox="0 0 14 10"><path d="M0 5h12M8 1l4 4-4 4" fill="none" stroke="#2aa3dc" stroke-width="1.4"/></svg></a>
    </div>
  </article>

  <article class="member" style="left:515px;top:903px">
    <div class="portrait"><div class="portrait-fill" role="img" aria-label="Portrait of the senior recruiter" style="background:linear-gradient(160deg,#a8a49c,#3e5a84)"></div></div>
    <div class="member-info" style="left:153px;top:-7px">
      <h3 class="member-name">Liam Foster</h3>
      <div class="member-role">Senior Recruiter</div>
      <p class="member-bio">Liam is a Senior Recruiter with over 14 years of IT, Financial and Healthcare recruiting experience in the NY and NJ market. He is a high energy professional with a strong background</p>
      <a class="learn-more" href="#">LEARN MORE <svg width="14" height="10" viewBox="0 0 14 10"><path d="M0 5h12M8 1l4 4-4 4" fill="none" stroke="#2aa3dc" stroke-width="1.4"/></svg></a>
    </div>
  </article>

  <footer class="site-footer">
    <p class="copyright">© 2016 Company Name&nbsp; All right reserved&nbsp; Term of Use</p>
    <div class="social"><span></span><span></span><span></span><span></span></div>
  </footer>
</div>
</body>
</html>
```